Business card for my company-RMK Design Studio

I do not have a logo-I like red and keeping it clean. Information that should be on the card:
Tom Brakefield AIA
Architecture Planning Interiors
Cell Phone-614.492.5068
email-rmkarchitect1@lunvale.com
www.rmkdesignstudio.net

```html
<!DOCTYPE html>
<html lang="en">
<head>
<meta charset="utf-8">
<title>RMK Design Studio – Business Card</title>
<link href="https://fonts.googleapis.com/css2?family=Libre+Baskerville:wght@700&family=Mulish:wght@400;500&display=swap" rel="stylesheet">
<style>
  :root {
    --bg: #2b2b2b;
    --red-light: #d62424;
    --red-mid: #b0221a;
    --red-dark: #7c0505;
    --ink: #ffffff;
  }
  * { box-sizing: border-box; margin: 0; padding: 0; }
  html, body { width: 1200px; height: 1200px; overflow: hidden; }
  body {
    background: var(--bg);
    display: flex;
    flex-direction: column;
    align-items: center;
    justify-content: center;
    gap: 48px;
    color: var(--ink);
  }
  .card {
    position: relative;
    width: 900px;
    height: 514px;
    background: linear-gradient(172deg, var(--red-light) 0%, var(--red-mid) 62%, var(--red-dark) 100%);
  }
  .name {
    font-family: "Libre Baskerville", Georgia, serif;
    font-weight: 700;
    line-height: 1.1;
    letter-spacing: 0.5px;
  }
  .rule {
    height: 3px;
    background: var(--ink);
  }
  .sans { font-family: "Mulish", Arial, sans-serif; }

  /* Front */
  .front .name { position: absolute; left: 56px; top: 110px; font-size: 54px; }
  .front .name .last { display: block; padding-left: 18px; }
  .front .rule { position: absolute; left: 72px; top: 262px; width: 132px; }
  .front .tagline { position: absolute; left: 80px; top: 282px; font-size: 21px; letter-spacing: 0.5px; }
  .contacts {
    position: absolute;
    left: 470px;
    top: 250px;
    list-style: none;
    display: flex;
    flex-direction: column;
    gap: 22px;
    font-size: 23px;
    letter-spacing: 0.8px;
    line-height: 1.2;
  }
  .contacts li { display: flex; align-items: flex-start; gap: 22px; }
  .contacts svg { flex: none; width: 26px; height: 26px; margin-top: 2px; }

  /* Back */
  .back { display: flex; flex-direction: column; align-items: center; justify-content: center; text-align: center; }
  .back .name { font-size: 58px; }
  .back .rule { width: 134px; margin: 26px 0 22px; }
  .back .web { font-size: 25px; letter-spacing: 1.5px; }
</style>
</head>
<body>

<section class="card front" aria-label="Card front">
  <h1 class="name">Tom<span class="last">Brakefield AIA</span></h1>
  <div class="rule"></div>
  <p class="tagline sans">Architecture Planning Interiors</p>
  <ul class="contacts sans">
    <li>
      <svg viewBox="0 0 26 26" fill="none" stroke="#fff" stroke-width="1.6" aria-hidden="true">
        <rect x="4" y="4" width="11" height="19"/>
        <rect x="15" y="11" width="7" height="12"/>
        <path d="M7 8h2M11 8h1M7 12h2M11 12h1M7 16h2M11 16h1M2 23h22"/>
      </svg>
      <span>418 17th Ave. #312 Harbor Point,<br>Ohio 4312</span>
    </li>
    <li>
      <svg viewBox="0 0 26 26" fill="none" stroke="#fff" stroke-width="1.8" aria-hidden="true">
        <rect x="7" y="2" width="12" height="22" rx="2"/>
        <path d="M11 20h4"/>
      </svg>
      <span>614.492.5068</span>
    </li>
    <li>
      <svg viewBox="0 0 26 26" fill="none" stroke="#fff" stroke-width="1.8" aria-hidden="true">
        <rect x="2" y="6" width="22" height="15" rx="1"/>
        <path d="M2 7l11 8 11-8"/>
      </svg>
      <span>rmkarchitect1@lunvale.com</span>
    </li>
  </ul>
</section>

<section class="card back" aria-label="Card back">
  <h2 class="name">Tom<br>Brakefield AIA</h2>
  <div class="rule"></div>
  <p class="web sans">www.rmkdesignstudio.net</p>
</section>

</body>
</html>
```